website refresh/redesign needed for Printing e commerce website

We'd like a website refresh/redesign done with the specific goal of having the site act as a more effective funnel for leads.<br/><br/>We think that the current design is outdated.<br/><br/>We want our customers and partners to still recognize the website, Is a big chunk of our business is repeat orders. <br/>so it should not be a full redesign. General color scheme and such should remain the same so that it is clear we are the same company. <br/><br/>However, the updated website design should look more polished and convey high-quality products and services that we provide. <br/><br/>Our website is https://shopledgerformsnet.paperquillprint.com/ if you want to take a look at our current website design. <br/><br/>we need 3 pages redesigned... <br/><br/>1. homepage:https://shopledgerformsnet.paperquillprint.com/<br/><br/>2. Category page: <br/>https://shopledgerformsnet.paperquillprint.com/order-computer-checks-c-4.html<br/><br/>3. Product detail page: https://shopledgerformsnet.paperquillprint.com/voucher-computer-checks-p-35.html<br/><br/> I can provide many more pictures of our products if needed.<br/><br/><br/>BTW. I have another project here on pixel bazaar, you can check the other ones too, so to make it easier to do both when working on this.<br/><br/> Please reach out to me should you have any questions or comments.
3 page

```html
<!DOCTYPE html>
<html lang="en">
<head>
<meta charset="utf-8">
<title>ShopLedgerForms – Business Check Printing</title>
<link href="https://fonts.googleapis.com/css2?family=Montserrat:wght@600;700;800&family=Poppins:wght@300;400;500;600&display=swap" rel="stylesheet">
<style>
:root{
  --green-dark:#1f4412;
  --green-head:#234d10;
  --green-logo:#8fd36a;
  --ink:#333;
  --muted:#777;
  --line:#d8d8d8;
  --band:#f1f1f1;
  --footer:#eeeeee;
  --white:#fff;
  --star:#f2c200;
}
*{box-sizing:border-box;margin:0;padding:0}
html,body{width:1200px;height:4142px;overflow:hidden}
body{font-family:'Poppins',sans-serif;color:var(--ink);background:var(--white);position:relative}
a{color:inherit;text-decoration:none}
.abs{position:absolute}
h2.section-title{font-family:'Montserrat',sans-serif;font-weight:700;color:var(--green-head);font-size:38px;letter-spacing:.2px}
.btn-outline{display:flex;align-items:center;justify-content:center;border:1.5px solid #555;background:var(--white);font-size:12px;color:#333}

/* header */
.topbar{position:absolute;left:0;top:0;width:1200px;height:87px;background:var(--green-dark)}
.brand{position:absolute;left:150px;top:28px;display:flex;align-items:center;gap:10px;font-family:'Poppins',sans-serif;font-weight:600;font-size:22px;color:var(--green-logo)}
.brand-dot{width:14px;height:14px;border-radius:50%;background:var(--green-logo)}
.account{position:absolute;right:147px;top:36px;display:flex;gap:28px;font-size:11px;color:#e8e8e8}
.account span{display:flex;align-items:center;gap:6px}
.navbar{position:absolute;left:0;top:87px;width:1200px;height:66px;background:var(--white);border-bottom:1px solid #e6e6e6}
.nav-links{position:absolute;left:150px;top:27px;display:flex;font-size:11px;color:#666}
.nav-links a{padding:0 12px;border-left:1px solid #ccc}
.nav-links a:first-child{padding-left:0;border-left:none}
.reorder{position:absolute;left:907px;top:101px;width:146px;height:39px;border:1.5px solid var(--green-dark);font-size:12px}

/* hero */
.hero{position:absolute;left:0;top:153px;width:1200px;height:519px}
.hero-bg{position:absolute;inset:0;background:linear-gradient(100deg,#f6f6f4 0%,#ecebe6 35%,#d9d7d0 60%,#f3f2ee 100%)}
.hero-text{position:absolute;left:148px;top:148px}
.hero-text .welcome{font-family:'Montserrat',sans-serif;font-weight:600;font-size:27px;color:var(--green-head)}
.hero-text h1{font-family:'Montserrat',sans-serif;font-weight:800;font-size:62px;line-height:56px;color:#222;margin-top:10px}
.hero-text h1 em{font-style:normal;color:var(--green-head);display:block}
.cart-panel{position:absolute;left:857px;top:69px;width:254px;height:376px;background:var(--white);box-shadow:0 4px 16px rgba(0,0,0,.08);text-align:center;padding-top:32px}
.cart-panel h3{font-weight:500;font-size:18px;color:var(--green-head)}
.field{width:176px;height:24px;margin:0 auto;border:1px solid var(--line);font-size:8px;color:#aaa;text-align:left;padding:6px 8px;position:relative}
.tabs{display:flex;justify-content:center;margin:40px 0 10px;font-size:12px;color:var(--green-head)}
.tabs span{padding:0 10px}
.tabs span+span{border-left:1px solid #ccc}
.check-btn{width:118px;height:32px;margin:14px auto 0;border:1.5px solid #555;font-size:12px;display:flex;align-items:center;justify-content:center}
.finder{margin-top:40px;font-size:13px;color:var(--green-head)}
.hero-arrow{position:absolute;left:1150px;top:236px}

/* check types */
.type{position:absolute;top:757px;width:414px}
.type .frame{margin-top:20px;width:414px;height:413px;border:2px solid #ddd;padding:22px}
.type .frame div{width:100%;height:100%}
.type ul{list-style:none;margin-top:14px;font-size:16px;line-height:22px;color:#444}

/* product cards */
.card{position:absolute;top:1401px;width:198px;height:353px;background:var(--white);box-shadow:0 3px 12px rgba(0,0,0,.12);text-align:center}
.card .thumb{height:88px}
.card h4{margin-top:24px;font-size:14px;font-weight:500;color:var(--green-head)}
.card .sub{font-size:7px;font-style:italic;color:#888;margin-top:2px}
.card p{font-size:9.5px;line-height:15px;color:#777;margin:20px 14px 0}
.card .price{font-size:9.5px;line-height:14px;color:#777;margin-top:16px}
.card .price b{display:block;font-weight:500;color:#444}
.card .btn-outline{width:114px;height:30px;margin:26px auto 0;font-size:11px;border-width:1px}

/* bands */
.band{position:absolute;left:0;width:1200px;background:var(--band)}
.band h2{text-align:center}
.thumb-row{position:absolute;left:150px;display:flex;gap:18px}
.layout-thumb{width:97px;height:64px;background:linear-gradient(180deg,#dfe8ee,#b6cfde)}
.soft-logo{width:93px;height:61px;background:linear-gradient(180deg,#fafafa,#dfe5ea);display:flex;align-items:center;justify-content:center;font-size:12px;font-weight:600;color:#2b4a7a;text-align:center}

/* about */
.about{position:absolute;left:150px;top:2250px;width:745px}
.about h2{font-family:'Montserrat',sans-serif;font-weight:800;font-size:58px;color:#222}
.about p{font-size:10px;line-height:20.5px;color:#666;margin-top:38px}
.about p+p{margin-top:8px}
.about .btn-outline{width:146px;height:39px;margin-top:40px;color:var(--green-head)}

/* reviews */
.reviews-title{position:absolute;left:148px;top:3166px;font-family:'Montserrat',sans-serif;font-weight:800;font-size:58px;color:#222}
.review-photo{position:absolute;left:150px;top:3325px;width:326px;height:282px;background:linear-gradient(135deg,#6a6a6a,#2e2e2e 60%,#8a8a8a)}
.review{position:absolute;left:507px;top:3334px;width:500px}
.review h3{font-family:'Montserrat',sans-serif;font-weight:700;font-size:34px;color:var(--green-head)}
.review .date{font-size:8px;color:#999;margin-top:8px}
.review p{font-size:10px;line-height:20.5px;color:#666;margin-top:24px}
.stars{display:flex;align-items:center;gap:4px;margin-top:14px;color:var(--star);font-size:15px}
.review .btn-outline{width:146px;height:39px;margin-top:30px;color:var(--green-head)}
.review-arrow{position:absolute;left:1100px;top:3444px}

/* footer */
.footer{position:absolute;left:0;top:3708px;width:1200px;height:360px;background:var(--footer)}
.fcol{position:absolute;top:82px}
.fcol h5{font-size:18px;font-weight:500;color:var(--green-head);margin-bottom:22px}
.fcol a{display:block;font-size:11px;color:#666;line-height:31px}
.social{display:flex;gap:6px}
.social i{width:18px;height:18px;border-radius:50%;display:block}
.fline{display:flex;align-items:center;gap:12px;font-size:11px;color:#666;line-height:27px}
.copyright{position:absolute;left:0;top:4068px;width:1200px;height:74px;border-top:1px solid #ddd;text-align:center;font-size:11px;color:#777;padding-top:28px}
</style>
</head>
<body>

<header class="topbar">
  <div class="brand"><span class="brand-dot"></span>ShopLedgerForms</div>
  <div class="account">
    <span><svg width="11" height="11" viewBox="0 0 12 12" fill="none" stroke="#e8e8e8" stroke-width="1.2"><rect x="1.5" y="2" width="8" height="8.5"/><path d="M5 6l6-5"/></svg>Register</span>
    <span><svg width="10" height="11" viewBox="0 0 10 12" fill="none" stroke="#e8e8e8" stroke-width="1.2"><rect x="1" y="5" width="8" height="6"/><path d="M2.8 5V3.3a2.2 2.2 0 014.4 0V5"/></svg>Log In</span>
  </div>
</header>

<nav class="navbar">
  <div class="nav-links">
    <a>Business Checks</a><a>Computer Checks</a><a>LedgerBook Checks</a><a>Accessories</a><a>Help/FAQs</a>
  </div>
</nav>
<a class="btn-outline reorder">Reorder</a>

<section class="hero">
  <div class="hero-bg" role="img" aria-label="Soft-focus photo of a laptop on a desk"></div>
  <div class="hero-text">
    <div class="welcome">Welcome To</div>
    <h1>Business Check <em>Printing</em></h1>
  </div>
  <aside class="cart-panel">
    <h3>View Your Cart</h3>
    <div class="field" style="margin-top:12px">Search By Software Checks
      <svg class="abs" style="right:7px;top:6px" width="10" height="10" viewBox="0 0 10 10" fill="none" stroke="#aaa"><circle cx="4" cy="4" r="3"/><path d="M6.3 6.3L9 9"/></svg></div>
    <div class="tabs"><span>Order Status</span><span>Contact Us</span></div>
    <div class="field" style="height:20px;padding-top:4px">Order Number</div>
    <div class="field" style="height:20px;padding-top:4px;margin-top:6px">Email Address</div>
    <div class="check-btn">Check</div>
    <div class="finder">Quick Finder</div>
    <div class="field" style="margin-top:8px;color:#555;border-color:#888">Checks By Software
      <svg class="abs" style="right:8px;top:8px" width="10" height="6" viewBox="0 0 10 6" fill="none" stroke="#555"><path d="M1 1l4 4 4-4"/></svg></div>
  </aside>
  <svg class="hero-arrow" width="20" height="32" viewBox="0 0 20 32" fill="none" stroke="#333" stroke-width="2"><path d="M4 3l12 13L4 29"/></svg>
</section>

<section>
  <div class="type" style="left:146px">
    <h2 class="section-title" style="padding-left:3px">Computer Checks</h2>
    <div class="frame"><div role="img" aria-label="Stack of colourful computer check sheets" style="background:linear-gradient(135deg,#f4f6f9 10%,#dbe9cf 40%,#cfd9ea 70%,#f1f1f1)"></div></div>
    <ul><li>• 100% Software Compatible</li><li>• Ships Within 24hr</li><li>• Free Logo</li></ul>
  </div>
  <div class="type" style="left:638px">
    <h2 class="section-title" style="padding-left:2px">Manual Checks</h2>
    <div class="frame" style="padding:56px 0 44px"><div role="img" aria-label="Three manual binder checks per page" style="background:linear-gradient(90deg,#f3f3f3 0 36%,#cfe2f0 36%,#eef4e4 75%,#cfe2f0)"></div></div>
    <ul><li>• Fits For 7 Ring Binder</li><li>• Ships Within 24hr</li><li>• Free Logo</li></ul>
  </div>
</section>

<section>
  <article class="card" style="left:93px">
    <div class="thumb" role="img" aria-label="Box of accounting checks" style="background:linear-gradient(135deg,#1e6e78,#e2a93a 60%,#1e6e78)"></div>
    <h4>LedgerBook Checks</h4><div class="sub">Voucher Checks - 3 Per Page - Wallet</div>
    <p>Order Custom Designed LedgerBooks Checks For Any Size Business.</p>
    <div class="price">LedgerBooks Checks Starts At<b>$12.99</b></div>
    <a class="btn-outline">See More</a>
  </article>
  <article class="card" style="left:367px">
    <div class="thumb" role="img" aria-label="Personal finance check pack" style="background:linear-gradient(135deg,#e9b9a6,#c8262a 55%,#8a1416)"></div>
    <h4>Quillet Checks</h4><div class="sub">Top Check - 3 On Page - Wallet</div>
    <p>Cheap Quillet Checks, Highest Quality Quillet Checks For Less.</p>
    <div class="price">Quillet Checks Starts At<b>$12.99</b></div>
    <a class="btn-outline">See More</a>
  </article>
  <article class="card" style="left:638px">
    <div class="thumb" role="img" aria-label="Deposit slip booklets" style="background:linear-gradient(90deg,#e8e9f1,#f7f7f7 55%,#7b3b5c)"></div>
    <h4>Deposit Slip</h4><div class="sub">Manual &amp; Computer Deposit Slips</div>
    <p>Manual &amp; Computer Deposit Slips Avail. In Single Copy, Duplicates, &amp; Triplicates.</p>
    <div class="price">Manual Deposit Slips At<b>$12.99</b></div>
    <a class="btn-outline">See More</a>
  </article>
  <article class="card" style="left:912px">
    <div class="thumb" role="img" aria-label="Self-inking stamp and envelopes" style="background:linear-gradient(90deg,#b4ad5c,#eef2ea 45%,#dbe9d0)"></div>
    <h4>Check Accessories</h4><div class="sub">Self-Inking Stamps - Envelopes</div>
    <p>Browse Our Fine Selection Of Check Envelopes &amp; Self-Inking Check Stamps.</p>
    <div class="price">Check Envelopes At<b>$9.99</b></div>
    <a class="btn-outline">See More</a>
  </article>
</section>

<section class="band" style="top:1849px;height:311px">
  <h2 class="section-title" style="margin-top:66px;font-size:35px">Checks By Layout</h2>
  <div class="thumb-row" style="top:169px">
    <div class="layout-thumb" role="img" aria-label="Single check layout"></div>
    <div class="layout-thumb" role="img" aria-label="Middle check layout"></div>
    <div class="layout-thumb" role="img" aria-label="Bottom check layout"></div>
    <div class="layout-thumb" role="img" aria-label="Three per page layout"></div>
    <div class="layout-thumb" role="img" aria-label="Wallet check layout"></div>
    <div class="layout-thumb" role="img" aria-label="Stub left layout"></div>
    <div class="layout-thumb" role="img" aria-label="Binder check layout"></div>
    <div class="layout-thumb" role="img" aria-label="Multi-stub layout"></div>
  </div>
</section>

<section class="about">
  <h2>Who We Are</h2>
  <p>Welcome To The Online Ordering System Of ShopLedgerForms.Net, Online Ordering At Shop Ledger Forms Provides The Most Comprehensive Business Check Experience And Selection Available Online, Including Traditional Manual Desktop Checks Used With The 7 Ring Check Binder, And An Extensive Selection Of Computer Checks. Our Computer Checks Are Available In Many Layout Styles And Colors, And Range From Layouts Compatible For Intellis LedgerBooks Software, Intellis Quillet To Checks Compatible With All Software Developed By Sorrel, Sorrel 50 Formerly Plumgrove, Sorrel 100 Formerly Plumgrove Accounting, Sorrel 100 Contractor (Formerly Sorrel Master Builder), Sorrel 100 ERP (Formerly Sorrel ERP 90 And 200) Sorrel 100 Fund Accounting (Formerly Fundline Accounting).</p>
  <p>ShopLedgerForms.Net Is The Leader In Tinted Security Check Envelopes, Signature Stamps For Checks, And Endorsement Stamps (For Deposit Only) Stamps. Shop Ledger Forms Set The Standard For Quality And Service. With Over A Decade Of Experience, The Team At Shop Ledger Forms Believes That The Only Way To Create Exceptional Business Checks Is Through A Total Team Effort. Our Widely-Skilled Team Consists Of Order Department And Customer Service, Checks Designers And Check Processioning And Printing, Shipping Department That Work With A Synergy, Enjoyed By Our Staff That Have A Vivid Passion For What They Do.</p>
  <a class="btn-outline">Read More</a>
</section>

<section class="band" style="top:2764px;height:311px">
  <h2 class="section-title" style="margin-top:73px;font-size:35px">Checks By Software</h2>
  <div class="thumb-row" style="top:166px;gap:23px">
    <div class="soft-logo">LedgerBooks</div>
    <div class="soft-logo">Quillet</div>
    <div class="soft-logo">Plumgrove</div>
    <div class="soft-logo">Sorrel</div>
    <div class="soft-logo">Metrodyne</div>
    <div class="soft-logo">TallyEdge</div>
    <div class="soft-logo">CodaPro</div>
    <div class="soft-logo">LeaseKeep</div>
  </div>
</section>

<section>
  <h2 class="reviews-title">Reviews</h2>
  <div class="review-photo" role="img" aria-label="Black and white portrait of a customer"></div>
  <div class="review">
    <h3>Nora | Portland</h3>
    <div class="date">03/23/2019</div>
    <p>A Great Place To Shop For Business Checks And Envelopes. Customer Service Is A+ The Checks Arrived Today, It Works Fine With Our Bookkeeping Software, The Same With The Window Envelopes. The Check Is Exquisitely Beautiful, The Paper Quality Is Also Very Good. Thank You, Great Seller. Five Star! What's Not To Love?</p>
    <div class="stars">
      <svg width="96" height="16" viewBox="0 0 96 16" fill="#f2c200"><g id="s"><path d="M8 0l2.4 5.2 5.6.6-4.2 3.8 1.2 5.6L8 12.4 3 15.2l1.2-5.6L0 5.8l5.6-.6z"/></g><use href="#s" x="20"/><use href="#s" x="40"/><use href="#s" x="60"/><use href="#s" x="80"/></svg>
      <span style="margin-left:14px;font-size:14px">5.0</span>
    </div>
    <a class="btn-outline">Read More</a>
  </div>
  <svg class="review-arrow" width="54" height="20" viewBox="0 0 54 20" fill="none" stroke="#222" stroke-width="2"><path d="M0 10h52M43 2l9 8-9 8"/></svg>
</section>

<footer class="footer">
  <div class="fcol" style="left:182px"><h5>Info</h5><a>Contact Us</a><a>Order History</a><a>Track Order</a><a>Help &amp; Support</a></div>
  <div class="fcol" style="left:399px"><h5>Support</h5><a>Shipping &amp; Turnaround</a><a>Help FAQs</a><a>Order Status</a><a>Reorder</a></div>
  <div class="fcol" style="left:646px"><h5>Information</h5><a>About Us</a><a>Privacy &amp; Security</a><a>Refunds &amp; Returns</a><a>Terms &amp; Conditions</a><a>Rush Order</a></div>
  <div class="fcol" style="left:875px"><h5>Stay In Touch</h5>
    <div class="social"><i style="background:#2d6cb5"></i><i style="background:#3b5ba0"></i><i style="background:#3aa3e3"></i><i style="background:#e0628a"></i></div>
    <div class="fline" style="margin-top:12px"><svg width="14" height="11" viewBox="0 0 14 11" fill="none" stroke="#777"><rect x=".5" y=".5" width="13" height="10"/><path d="M.5 .5l6.5 5 6.5-5"/></svg>Get Our News Letter</div>
    <div class="fline"><svg width="13" height="14" viewBox="0 0 13 14" fill="none" stroke="#777"><path d="M6.5 .5l5.5 2v4c0 3.5-2.5 6-5.5 7C3.5 12.5 1 10 1 6.5v-4z"/></svg>100% Safe</div>
  </div>
</footer>
<div class="copyright">Copyright © 2017 Shop Ledger Forms.Net | Sitemap</div>

</body>
</html>
```